December online webinar for our coaching and mentoring business.

needing an email flyer and something to use on appropriate social media e.g. Instagram to promote our December half day webinar focusing on positive mindset, relationships and 2021 being a new year with new opportunities. For the feel of what we have done previously:
www.qlvgetaways.com.au
We will be using 2 guest speakers:
Dominic Farrow of 60Quests.com and
Marisa Holt, psychologist and both will need to be prominent on the marketing material we send out on email and use on social media.
The webinar will likely run Thursday December 10th from 12.30pm to 4.30pm AEST and will be hosted and facilitated by me and on behalf of Portwell Business Coaching.
I am thinking colour schemes and branding similar to what you see on the website above.
Pricing needs to be on the flyer - $750 + GST per person*
*enquire for multi booking discounts for 2 people or more

Target Market(s)

people looking for a boost before the year end and a fast start to 2021

Font styles to use
Sans Serif

Requirements
Must have
• see brief above
Nice to have
• see brief above
Should not have
• see brief above

```html
<!DOCTYPE html>
<html lang="en">
<head>
<meta charset="utf-8">
<title>Webinar Coaching and Mentoring Business – Flyer</title>
<link href="https://fonts.googleapis.com/css2?family=Bebas+Neue&family=Open+Sans:ital,wght@0,400;0,600;0,700;1,400&display=swap" rel="stylesheet">
<style>
  :root {
    --page: #ffffff;
    --ink: #231f20;
    --ink-light: #3a3536;
    --red: #ef4136;
    --red-deep: #962225;
    --red-mid: #c4262b;
    --red-box: #ff2d2d;
    --red-dark-text: #3d0b0b;
    --white: #ffffff;
    --photo-yellow: #f2d21b;
    --photo-grey: #e4e1dc;
  }
  * { margin: 0; padding: 0; box-sizing: border-box; }
  html, body { width: 1200px; height: 1200px; overflow: hidden; background: var(--page); }
  .flyer {
    position: absolute; left: 206px; top: 58px; width: 795px; height: 1091px;
    background: linear-gradient(160deg, var(--ink) 0%, var(--ink-light) 30%, var(--ink) 55%, #2b2728 80%, var(--ink) 100%);
    overflow: hidden; color: var(--white);
    font-family: "Open Sans", sans-serif;
  }
  .flyer-shapes { position: absolute; inset: 0; }
  .brand {
    position: absolute; left: 24px; top: 40px; width: 200px;
    font-family: "Open Sans", sans-serif; font-weight: 700; font-size: 26px; line-height: 1.1;
    color: var(--white);
  }
  .headline {
    position: absolute; right: 28px; top: 100px; text-align: right;
    font-family: "Bebas Neue", sans-serif; font-size: 70px; line-height: 66px; letter-spacing: 0.5px;
    text-shadow: 2px 3px 6px rgba(0,0,0,0.5);
  }
  .topic {
    position: absolute; left: 0; right: 0; top: 276px; text-align: center;
    font-family: "Bebas Neue", sans-serif; font-size: 46px; line-height: 52px;
    text-shadow: 2px 3px 6px rgba(0,0,0,0.5);
  }
  .topic .accent { color: var(--red); }
  .divider { position: absolute; left: 131px; width: 552px; top: 388px; height: 1.5px; background: var(--white); }
  .speakers-intro {
    position: absolute; left: 0; right: 0; top: 404px; text-align: center;
    font-weight: 600; font-size: 29px;
  }
  .speaker { position: absolute; top: 505px; width: 300px; text-align: center; }
  .speaker--one { left: 110px; }
  .speaker--two { left: 387px; }
  .speaker-photo {
    width: 244px; height: 244px; margin: 0 auto; border-radius: 50%;
    border: 5px solid var(--white);
  }
  .speaker--one .speaker-photo { background: radial-gradient(circle at 50% 40%, #555 0%, #3a3a3a 35%, var(--photo-yellow) 36%, #eccb12 100%); }
  .speaker--two .speaker-photo { background: radial-gradient(circle at 50% 45%, #2a6f9e 0%, #1f5c88 35%, #f3e7a0 50%, var(--photo-grey) 100%); }
  .speaker-name { margin-top: 8px; color: var(--red); font-weight: 600; font-size: 30px; line-height: 36px; }
  .speaker-role { font-size: 19px; line-height: 22px; }
  .date-box {
    position: absolute; left: 167px; top: 835px; width: 464px; height: 105px;
    background: var(--red-box); text-align: center; font-weight: 700; font-size: 33px; line-height: 44px;
    padding-top: 8px;
  }
  .date-box .day { color: var(--red-dark-text); }
  .price {
    position: absolute; left: 0; right: 0; top: 952px; text-align: center;
    font-weight: 600; font-size: 48px; letter-spacing: -1.5px;
    text-shadow: 2px 3px 6px rgba(0,0,0,0.5);
  }
  .fine-print {
    position: absolute; left: 90px; top: 1055px; width: 618px; height: 40px; border-radius: 20px;
    background: var(--white); color: var(--ink); text-align: center;
    font-style: italic; font-size: 21px; line-height: 40px;
  }
</style>
</head>
<body>
<main class="flyer">
  <svg class="flyer-shapes" viewBox="0 0 795 1091" aria-hidden="true">
    <g stroke="rgba(255,255,255,0.08)" stroke-width="1.5">
      <line x1="200" y1="20" x2="795" y2="280"/>
      <line x1="250" y1="100" x2="795" y2="340"/>
      <line x1="0" y1="900" x2="500" y2="1091"/>
      <line x1="0" y1="960" x2="380" y2="1091"/>
    </g>
    <polygon points="0,0 380,0 0,268" fill="var(--red)"/>
    <polygon points="614,381 795,467 795,620 725,589 688,476 655,492" fill="var(--red-deep)"/>
    <polygon points="688,476 795,530 795,560 712,527" fill="var(--red-mid)"/>
    <polyline points="614,381 655,492 795,560" fill="none" stroke="var(--red)" stroke-width="1.5"/>
    <polygon points="0,619 18,625 56,740 0,715" fill="var(--red-deep)"/>
    <polygon points="0,673 109,726 149,839 0,770" fill="var(--red-deep)"/>
    <polygon points="0,690 45,712 56,740 0,715" fill="var(--red-mid)"/>
    <polyline points="0,770 149,839" fill="none" stroke="var(--red)" stroke-width="1.5"/>
  </svg>

  <div class="brand">Portwell Business Coaching</div>

  <h1 class="headline">Webinar Coaching<br>and Mentoring Business</h1>

  <h2 class="topic">Positive Mindset, Relationships and 2021<br>Being a <span class="accent">New Year with New Opportunities</span></h2>

  <div class="divider"></div>

  <p class="speakers-intro">with 2 Guest Speakers:</p>

  <section class="speaker speaker--one">
    <div class="speaker-photo" role="img" aria-label="Portrait photo of guest speaker Dominic Farrow on a yellow background"></div>
    <p class="speaker-name">Dominic Farrow</p>
    <p class="speaker-role">of 60Quests.com</p>
  </section>

  <section class="speaker speaker--two">
    <div class="speaker-photo" role="img" aria-label="Portrait photo of guest speaker Marisa Holt, psychologist, seated in a bright room"></div>
    <p class="speaker-name">Marisa Holt</p>
    <p class="speaker-role">Psychologist</p>
  </section>

  <div class="date-box">
    <div class="day">Thursday December 10th</div>
    <div class="time">12.30pm to 4.30pm AEST</div>
  </div>

  <p class="price">$750 + GST per person*</p>

  <p class="fine-print">*enquire for multi booking discounts for 2 people or more</p>
</main>
</body>
</html>
```